Wordpress Powered Website. Outstanding Design Required. Using Morvenix Theme

Designers will not need to create anything other than the home page but there are some design elements on the home page which also need to be factored in: 6 product place holders and 2-3 slides for a slideshow (with images I provide).

Designers will need to familiarise themselves with the Morvenix theme to make sure that their design will work within the theme.

The winning designer will set up all the pages and navigation in place. This includes social media icons, favicon, widgets, etc. In other words, the home page needs to be designed and coded and the other preset theme pages need to be organised in a way that we can start using the website on completion of the job.

Most of the designs I had last time were too colourful. This needs to be subtle not in your face.

Background to the business/website:
Tandrel Banners is a new Australian venture which will sell large format printed banners and other signage. The market is very competitive so it is important to stand out visually and to have a website which is clean, easy to navigate and easy to order. It will be a combination of online sales and assisted sales but all sales enquiries will come from the website.

As our business is focused on presentation it is vital to have excellent design.
Purchased theme is Morvenix. Only this theme is to be used.

1. A home page using all the preset features of the Morvenix theme - it will just be basically taking my wireframe and inputting it to the live theme.
2. A three slide slideshow, ideally with an edited video. The static image slides can be provided by me during the handover. Placeholder for now.
Similar to this one: http://thebrindlecraft.com.au/

Attached is the logo which must be utilised, although it could also sit on a dark background. There is our mascot as well which can be used but does not have to be included.

Target Market(s)

Primarily B2B (business to business)
Main industries will be Construction, Retail, Community, Events & Trade Shows

Industry/Entity Type

Printing

Coding

Coded - Design and coding required

Font styles to use
Sans Serif

Requirements
Must have
• Must have the design files made to web pages within the Wordpress environment.
Nice to have
• Clean design. Stand out from competitors based on design.
Should not have
• Should not look like any competitor

```html
<!DOCTYPE html>
<html lang="en">
<head>
<meta charset="utf-8">
<title>Tandrel Banners</title>
<link href="https://fonts.googleapis.com/css2?family=Exo+2:wght@300;400;600;700;800&family=Arimo:wght@400;700&display=swap" rel="stylesheet">
<style>
:root{
  --red:#e31e24;
  --orange:#f15a22;
  --blue:#1a6fb5;
  --green:#3ea83a;
  --amber:#f58220;
  --ink:#2b2b2b;
  --muted:#555;
  --grey-band:#ececec;
  --card-frame:#d9d9d9;
  --footer:#2a2a2a;
  --yellow:#ffd200;
}
*{box-sizing:border-box;margin:0;padding:0}
html,body{width:1200px;height:3175px;overflow:hidden;background:#fff}
body{font-family:"Arimo",Arial,sans-serif;color:var(--ink);position:relative}
.abs{position:absolute}

/* header */
.site-header{position:absolute;left:0;top:0;width:1200px;height:100px;background:#fff}
.brand{position:absolute;left:48px;top:24px;display:flex;align-items:center;gap:12px}
.brand-dot{width:22px;height:22px;border-radius:50%;background:var(--red)}
.brand-name{font-family:"Exo 2",sans-serif;font-weight:800;font-size:34px;color:var(--red);letter-spacing:.5px}
.contact-list{position:absolute;left:930px;top:18px;list-style:none;font-size:14px;color:#444;line-height:22px}
.contact-list li{display:flex;align-items:center;gap:8px}
.contact-list svg{flex:none}

.main-nav{position:absolute;left:0;top:100px;width:1200px;height:50px;background:var(--red)}
.nav-item{position:absolute;top:17px;color:#fff;font-size:13px;text-transform:uppercase;letter-spacing:.3px}

/* hero */
.hero{position:absolute;left:0;top:150px;width:1200px;height:508px;background:linear-gradient(180deg,#6f7478 0%,#9ea2a4 45%,#b9bcbc 70%,#8d8f8e 100%)}
.hero-box{position:absolute;left:55px;top:106px;width:545px;height:274px;background:rgba(30,30,30,.82);padding:22px 0 0 16px}
.hero-kicker{font-family:"Exo 2",sans-serif;font-weight:800;font-size:39px;color:var(--yellow);line-height:42px;letter-spacing:.5px}
.hero-title{font-family:"Exo 2",sans-serif;font-weight:400;font-size:36px;color:#fff;line-height:35px;text-transform:uppercase;letter-spacing:.5px}
.hero-points{list-style:none;margin-top:18px;font-size:15px;color:#fff;line-height:27px}
.hero-points li{display:flex;align-items:center;gap:8px}

/* section titles */
.section-title{position:absolute;left:0;width:1200px;text-align:center;font-family:"Exo 2",sans-serif;font-weight:300;font-size:34px;letter-spacing:2px;color:#333}
.title-rule{position:absolute;left:555px;width:90px;height:2px;background:#bbb}

/* services */
.service{position:absolute;top:775px;width:240px;text-align:center}
.service-ring{width:156px;height:156px;border-radius:50%;margin:0 auto;border:9px solid;display:flex;align-items:center;justify-content:center}
.service-core{width:92px;height:92px;border-radius:50%;display:flex;align-items:center;justify-content:center}
.service-name{font-family:"Arimo",sans-serif;font-weight:700;font-size:18px;margin-top:30px;letter-spacing:1.2px;color:#222}
.service-text{font-size:12.5px;line-height:21px;color:#555;margin:12px auto 0;width:225px}
.service-rule{width:215px;height:2px;margin:22px auto 0}

/* products */
.product-tabs{position:absolute;top:1253px;left:250px;width:740px;height:66px;display:flex}
.tab{width:222px;height:66px;display:flex;align-items:center;justify-content:center;font-size:14px;text-transform:uppercase;color:#222}
.tab.is-active{background:var(--orange);color:#fff;width:256px;position:relative}
.tab.is-active::after{content:"";position:absolute;left:116px;bottom:-14px;border:12px solid transparent;border-top-color:var(--orange);border-bottom:0}
.tab.is-last{width:270px}
.products-band{position:absolute;left:0;top:1319px;width:1200px;height:342px;background:var(--grey-band)}
.product-card{position:absolute;width:245px;background:#fff}
.product-frame{background:var(--card-frame);padding:14px;height:196px}
.product-photo{height:168px}
.product-caption{height:80px;text-align:center;padding-top:16px}
.product-name{font-weight:700;font-size:15px;color:#222}
.product-meta{font-size:12px;color:#444;margin-top:6px}
.product-card.is-featured .product-caption{background:var(--orange)}
.product-card.is-featured .product-name,.product-card.is-featured .product-meta{color:#fff}

/* promo band */
.promo{position:absolute;left:0;top:2033px;width:1200px;height:507px;background:var(--red);text-align:center;color:#fff}
.promo-title{font-family:"Exo 2",sans-serif;font-weight:700;font-size:28px;margin-top:48px;letter-spacing:.5px}
.promo-text{font-family:"Exo 2",sans-serif;font-size:23px;line-height:32px;margin:16px auto 0;width:1080px}

/* map */
.map{position:absolute;left:0;top:2540px;width:1200px;height:356px;background:linear-gradient(135deg,#e6e4dd 0%,#efede6 55%,#a9c6e8 75%,#b7cfe9 100%)}

/* footer */
.site-footer{position:absolute;left:0;top:2896px;width:1200px;height:279px;background:var(--footer);color:#fff}
.footer-col{position:absolute;top:44px}
.footer-col h4{font-family:"Arimo",sans-serif;font-size:14px;font-weight:700;text-transform:uppercase;letter-spacing:.4px}
.footer-col ul{list-style:none;margin-top:14px;font-size:13px;line-height:25px;color:#ddd}
.footer-col li::before{content:"» ";color:#fff}
.social{display:flex;gap:12px;margin-top:22px}
.social span{width:46px;height:46px;background:#3d3d3d;display:block}
.footer-bar{position:absolute;left:0;top:212px;width:1200px;height:60px}
.assurance{position:absolute;top:8px;display:flex;align-items:center;gap:10px;font-size:12.5px;font-weight:700;text-transform:uppercase;line-height:16px}
.copyright{position:absolute;left:833px;top:24px;font-size:12.5px;color:#ddd}
</style>
</head>
<body>

<header class="site-header">
  <div class="brand"><span class="brand-dot"></span><span class="brand-name">Tandrel Banners</span></div>
  <ul class="contact-list">
    <li><svg width="12" height="14" viewBox="0 0 12 14"><path d="M6 0a5 5 0 0 1 5 5c0 4-5 9-5 9S1 9 1 5a5 5 0 0 1 5-5z" fill="#f15a22"/><circle cx="6" cy="5" r="2" fill="#fff"/></svg>Address: Larkvale, Victoria</li>
    <li><svg width="14" height="10" viewBox="0 0 14 10"><rect width="14" height="10" fill="#f15a22"/><path d="M0 0l7 6 7-6" stroke="#fff" fill="none"/></svg>Email: info@tandrelbanners.com</li>
    <li><svg width="10" height="14" viewBox="0 0 10 14"><rect width="10" height="14" rx="2" fill="#f15a22"/><rect x="2" y="2" width="6" height="8" fill="#fff"/></svg>Phone: 1300 472 918</li>
  </ul>
</header>

<nav class="main-nav">
  <span class="nav-item" style="left:82px">Home</span>
  <span class="nav-item" style="left:189px">Banners</span>
  <span class="nav-item" style="left:314px">Flags</span>
  <span class="nav-item" style="left:421px">Banners Stands</span>
  <span class="nav-item" style="left:597px">Signs</span>
  <span class="nav-item" style="left:701px">Contact Us</span>
  <span class="nav-item" style="left:847px">About Us</span>
  <span class="nav-item" style="left:978px">FAQs</span>
</nav>

<section class="hero" role="img" aria-label="Slideshow photo: man in a white shirt throwing bright paint splashes over a grey city skyline">
  <div class="hero-box">
    <div class="hero-kicker">OVER 95%</div>
    <div class="hero-title">Customers recommend<br>us to their friends</div>
    <ul class="hero-points">
      <li><svg width="12" height="12" viewBox="0 0 12 12"><path d="M1 6l3.5 3.5L11 2" stroke="#fff" stroke-width="2" fill="none"/></svg>Super Fast Turn Around</li>
      <li><svg width="12" height="12" viewBox="0 0 12 12"><path d="M1 6l3.5 3.5L11 2" stroke="#fff" stroke-width="2" fill="none"/></svg>No Set-up Fees</li>
      <li><svg width="12" height="12" viewBox="0 0 12 12"><path d="M1 6l3.5 3.5L11 2" stroke="#fff" stroke-width="2" fill="none"/></svg>Lowest Price Guaranteed</li>
      <li><svg width="12" height="12" viewBox="0 0 12 12"><path d="M1 6l3.5 3.5L11 2" stroke="#fff" stroke-width="2" fill="none"/></svg>Over 95% Customer Satisfaction</li>
    </ul>
  </div>
</section>

<h2 class="section-title" style="top:686px">OUR SERVICES</h2>
<div class="title-rule" style="top:738px"></div>

<div class="service" style="left:62px">
  <div class="service-ring" style="border-color:var(--blue)"><div class="service-core" style="background:var(--blue)">
    <svg width="44" height="44" viewBox="0 0 44 44"><rect x="20" y="14" width="12" height="24" rx="2" fill="#fff"/><rect x="23" y="9" width="6" height="5" fill="#fff"/><path d="M8 12h8M6 18h10M8 24h8" stroke="#fff" stroke-width="2"/></svg>
  </div></div>
  <div class="service-name">Free Design Service</div>
  <p class="service-text">Our vinyl banners price includes free basic design. Our excellent graphic designers can put your dreams into reality.</p>
  <div class="service-rule" style="background:var(--blue)"></div>
</div>
<div class="service" style="left:341px">
  <div class="service-ring" style="border-color:var(--green)"><div class="service-core" style="background:var(--green)">
    <svg width="44" height="44" viewBox="0 0 44 44"><rect x="10" y="6" width="24" height="32" rx="2" fill="#fff"/><circle cx="22" cy="20" r="7" fill="#3ea83a"/><path d="M17 38l5-6 5 6" fill="#3ea83a"/></svg>
  </div></div>
  <div class="service-name">Ensure Quality</div>
  <p class="service-text">Our vinyl banners price includes free basic design. Our excellent graphic designers can put your dreams into reality.</p>
  <div class="service-rule" style="background:var(--green)"></div>
</div>
<div class="service" style="left:617px">
  <div class="service-ring" style="border-color:var(--amber)"><div class="service-core" style="background:var(--amber)">
    <svg width="48" height="40" viewBox="0 0 48 40"><rect x="4" y="10" width="26" height="18" fill="#fff"/><path d="M30 15h8l6 7v6H30z" fill="#fff"/><circle cx="12" cy="30" r="4" fill="#fff" stroke="#f58220" stroke-width="2"/><circle cx="36" cy="30" r="4" fill="#fff" stroke="#f58220" stroke-width="2"/></svg>
  </div></div>
  <div class="service-name">Fast Delivery</div>
  <p class="service-text">Our vinyl banners price includes free basic design. Our excellent graphic designers can put your dreams into reality.</p>
  <div class="service-rule" style="background:var(--amber)"></div>
</div>
<div class="service" style="left:892px">
  <div class="service-ring" style="border-color:var(--red)"><div class="service-core" style="background:var(--red)">
    <svg width="44" height="44" viewBox="0 0 44 44"><circle cx="22" cy="18" r="12" fill="#fff"/><text x="22" y="24" text-anchor="middle" font-family="Arimo,sans-serif" font-weight="700" font-size="16" fill="#e31e24">$</text><rect x="6" y="30" width="32" height="7" fill="#fff"/></svg>
  </div></div>
  <div class="service-name">Price Guarantee</div>
  <p class="service-text">Our vinyl banners price includes free basic design. Our excellent graphic designers can put your dreams into reality.</p>
  <div class="service-rule" style="background:var(--red)"></div>
</div>

<h2 class="section-title" style="top:1180px">OUR PRODUCTS</h2>
<div class="title-rule" style="top:1232px"></div>

<div class="product-tabs">
  <div class="tab">Popular</div>
  <div class="tab is-active">New Arrivals</div>
  <div class="tab is-last">Best Sellers</div>
</div>

<div class="products-band"></div>

<div class="product-card is-featured" style="left:55px;top:1355px">
  <div class="product-frame"><div class="product-photo" role="img" aria-label="Product photo: fabric banner for a fast food promotion" style="background:linear-gradient(135deg,#c9312e,#e8d9c9 60%,#8a6b4e)"></div></div>
  <div class="product-caption"><div class="product-name">Cloth / Fabric Banners</div><div class="product-meta">600mm x 1200mm Starts at $42.55</div></div>
</div>
<div class="product-card" style="left:330px;top:1355px">
  <div class="product-frame"><div class="product-photo" role="img" aria-label="Product photo: health clinic billboard" style="background:linear-gradient(180deg,#7fb2dc,#d33a4a 55%,#5f8a3f)"></div></div>
  <div class="product-caption"><div class="product-name">Cloth / Fabric Banners</div><div class="product-meta">600mm x 1200mm Starts at $42.55</div></div>
</div>
<div class="product-card" style="left:610px;top:1355px">
  <div class="product-frame"><div class="product-photo" role="img" aria-label="Product photo: red roadside billboard under blue sky" style="background:linear-gradient(180deg,#2e78c9,#b9262b 55%,#3a6fb6)"></div></div>
  <div class="product-caption"><div class="product-name">Cloth / Fabric Banners</div><div class="product-meta">600mm x 1200mm Starts at $42.55</div></div>
</div>
<div class="product-card" style="left:880px;top:1355px">
  <div class="product-frame"><div class="product-photo" role="img" aria-label="Product photo: billboard in a green field" style="background:linear-gradient(180deg,#3b7fc4,#8db7de 55%,#5e9a3a)"></div></div>
  <div class="product-caption"><div class="product-name">Cloth / Fabric Banners</div><div class="product-meta">600mm x 1200mm Starts at $42.55</div></div>
</div>

<div class="product-card" style="left:55px;top:1710px">
  <div class="product-frame"><div class="product-photo" role="img" aria-label="Product photo: outdoor building banner" style="background:linear-gradient(135deg,#2f6fb4,#d89b34 55%,#f1f1f1)"></div></div>
  <div class="product-caption"><div class="product-name">Cloth / Fabric Banners</div><div class="product-meta">600mm x 1200mm Starts at $42.55</div></div>
</div>
<div class="product-card" style="left:330px;top:1710px">
  <div class="product-frame"><div class="product-photo" role="img" aria-label="Product photo: illuminated street billboard at night" style="background:linear-gradient(135deg,#141820,#5c6a80 50%,#c66a2c)"></div></div>
  <div class="product-caption"><div class="product-name">Cloth / Fabric Banners</div><div class="product-meta">600mm x 1200mm Starts at $42.55</div></div>
</div>
<div class="product-card" style="left:610px;top:1710px">
  <div class="product-frame"><div class="product-photo" role="img" aria-label="Product photo: red roadside billboard under blue sky" style="background:linear-gradient(180deg,#2e78c9,#b9262b 55%,#3a6fb6)"></div></div>
  <div class="product-caption"><div class="product-name">Cloth / Fabric Banners</div><div class="product-meta">600mm x 1200mm Starts at $42.55</div></div>
</div>
<div class="product-card" style="left:880px;top:1710px">
  <div class="product-frame"><div class="product-photo" role="img" aria-label="Product photo: red shopfront sign on a wide billboard" style="background:linear-gradient(180deg,#dfe6ec,#c4262b 50%,#9aa39a)"></div></div>
  <div class="product-caption"><div class="product-name">Cloth / Fabric Banners</div><div class="product-meta">600mm x 1200mm Starts at $42.55</div></div>
</div>

<section class="promo">
  <h2 class="promo-title">CUSTOM BANNER PRINTING, DISPLAYS, SIGNS &amp; GRAPHICS</h2>
  <p class="promo-text">Our Banners are constructed of durable vinyl and printed with the latest technology in commercial printers. We provide a wide range of banner sizes - up to 100 feet long</p>
  <div class="abs" role="img" aria-label="Film strip of sample banner images" style="left:165px;top:250px;width:870px;height:150px;background:linear-gradient(90deg,#1b1b1b,#6b5a44 20%,#222 45%,#222 55%,#8a6a3a 80%,#1b1b1b);border-radius:6px"></div>
  <svg class="abs" style="left:418px;top:212px" width="364" height="262" viewBox="0 0 364 262" role="img" aria-label="Monitor showing a gallery of banner samples">
    <rect x="0" y="0" width="364" height="222" rx="6" fill="#2b2b2b"/>
    <rect x="12" y="12" width="340" height="196" fill="#5a7fae"/>
    <path d="M160 222h44l10 28h-64z" fill="#1e1e1e"/>
    <rect x="120" y="248" width="124" height="8" rx="3" fill="#1e1e1e"/>
  </svg>
</section>

<section class="map" role="img" aria-label="Street map showing the office location"></section>

<footer class="site-footer">
  <div class="footer-col" style="left:100px"><h4>Main Menu</h4><ul><li>Home</li><li>What's New?</li><li>Featured</li><li>Top sellers</li></ul></div>
  <div class="footer-col" style="left:303px"><h4>Extras</h4><ul><li>Specials</li><li>Brands</li><li>Reviews</li></ul></div>
  <div class="footer-col" style="left:497px"><h4>Information</h4><ul><li>Privacy Policy</li><li>Contacts</li><li>Terms &amp; Conditions</li></ul></div>
  <div class="footer-col" style="left:673px"><h4>Your Account</h4><ul><li>Shipping &amp; Returns</li><li>Advanced Search</li><li>Create an Account</li><li>Log in</li></ul></div>
  <div class="footer-col" style="left:895px"><h4>Follow Us On</h4><div class="social"><span></span><span></span><span></span></div></div>

  <div class="footer-bar">
    <div class="assurance" style="left:92px">
      <svg width="34" height="30" viewBox="0 0 34 30"><rect x="2" y="12" width="7" height="16" fill="#fff"/><path d="M11 13l7-11c3 0 4 2 3 6l-1 3h10c2 0 3 2 2 4l-4 11c-1 2-2 2-4 2H11z" fill="#fff"/></svg>
      <span>Satisfaction<br>100% Guaranteed</span>
    </div>
    <div class="assurance" style="left:282px">
      <svg width="40" height="28" viewBox="0 0 40 28"><rect x="2" y="4" width="22" height="16" fill="#fff"/><path d="M24 9h7l6 6v5H24z" fill="#fff"/><circle cx="9" cy="22" r="4" fill="#fff" stroke="#2a2a2a" stroke-width="2"/><circle cx="30" cy="22" r="4" fill="#fff" stroke="#2a2a2a" stroke-width="2"/></svg>
      <span>Free Shipping<br>On Orders Over $99</span>
    </div>
    <div class="assurance" style="left:488px">
      <svg width="32" height="30" viewBox="0 0 32 30"><path d="M27 11A12 12 0 0 0 5 10M5 19a12 12 0 0 0 22 1" stroke="#fff" stroke-width="3.5" fill="none"/><path d="M29 3v9h-9zM3 27v-9h9z" fill="#fff"/></svg>
      <span>7 Day<br>Easy Return</span>
    </div>
    <div class="copyright">Copyright © 2016 Tandrel Banners. All Rights Reserved</div>
  </div>
</footer>

</body>
</html>
```